Greek Souvlaki Restaurant Menu Design

We would like to redesign our menu (at the moment just a price-list without any graphics) and create something more fun.

You can find all the items we are offering at the following link / our e-shop:
https://olivebranchkitchen.example/orders/en/order/
I have also attached a printout of the above with hand written notes on the sections and items that will be included.

Our menu is divided to a couple of parts:
- Souvlaki Bar and Grill
- Authentic Greek Cuisine
- Wine List
- Desserts
- Bakaliko

This project will take on the first part of our menu, which is the Souvlaki Bar and Grill. If we are happy with your design, we will then develop the rest of our menu.

Souvlaki Bar and Grill
---------------------------

Our souvlaki can be customised to the customer requirements. The following links have similar set ups:

WOW!Patty
https://gr.pinboardly.example/pin/100000000000000001/
I like the way they have set it up, but the graphics and colours used are not my thing. I also like they way they have split up the steps, choose, top it of, etc.

The Krokk
https://gr.pinboardly.example/pin/100000000000000002/
I hate the step 1,2,3 on the left side. It does not make it playful. Like the fact that they have used pictures of the ingredients.

https://gr.pinboardly.example/pin/100000000000000003/
Hate the graphics, like the concept.

-------------

First Sections: Our Souvliaki Pita Wrap

The steps to customise a souvlaki can be found on the following link:
https://olivebranchkitchen.example/orders/en/order/ and choose pita wrap.

Most of the one side of our Souvliaki/Grill menu should be dedicated to our Pita Wraps.

It should have a small description of the Greek Souvlaki Pita Wrap. Something along the lines of "Get a whole meal all wrapped up with our delicious Greek Pita Wraps. Containing protein, sauce and salad". Improvements of this line are welcome.

It should then have the steps to customise it.

Step One.
Choose Base:
1. Chicken Skewer
2. Pork Skewer
3. etc
Price and options can be found on the above link on our website

Step Two.
Add one of our delicious home made sauces.
Options can be found on our website.

Step Three
Finalise it with the ingredients of your choice.
The customer can select multiple incredients

Step Four.
Feeling Hungry? Add extras:
Extras and Prices can be found on the link provided.

Buy two wraps and save. Takeaway only!
You will find this option as "Double Souvlaki Pita Wrap Offer."
Instead of 2x5.5 = £11 pay £10.5. This offer should also be mentioned somewhere on this section.

-----

Second Section - Our Platters

Skewers Platter and Gyros Platter

Options can be found by clicking on the items on the link provided.

Extras and Pita Bread option are common. Meat options are different and skewers have a choice of side. Meat options have 2/3 skewers and 200/300 grams of gyros, so they can probably be combined somehow.

These section can also be called Naked / Open Souvlaki Platters

Third Section
From Our Grill

All options from this section together with modifiers (can be see if you click on each item). I would like pictures from each item.

Forth Section
Meal Deals, starter combo and Set Menu.

Meal Deal for 1/2 and 4 are wraps with extras. The for 4 is not on the pdf and will be up on our website soon, so please check. I think those are easy to e incorporated next to the pita wrap section as upgrades to save.

Set menus are various items.

If they can fit on this page somehow we incorporate them, if not we can make a separate page with the offers / meals deals. If a separate page is created them the meal deal from our kitchen and vegetarean set menu should also be included.

Fifth Section
Salads and Starter

I would like all options from Hot and Cold starter and our salad. I would like pictures next to all options, if possible.

-----

Final notes/ideas.

Wraps, platters and grill could be one page front and back. Salads and starters could be a different page(s) or sections.

The menu should be easily updated and we would like a format where we can update prices and descriptions.

Prices and descriptions can be found on the link provided.

Feel free to improve our descriptions and titles. Please do mention where you made improvements, so we can approve them.

Our kitchen, dessert and wine menu will be given as a separate project and priority will be given to the person that won this competition.

If you need better quality pictures please let us know, most of the pictures we do have them in raw format too.

------

Some designs that I like. To give you an idea of the design I would like to see:

https://www.craftmarketly.example/listing/100000001/american-menu-restaurant-cafe-menus
I would love to see something like that for the grill/salad/starter side of our menu, since it has space for pictures.

https://gr.pinboardly.example/pin/100000000000000004/
I would love to see something like that, where the incredients of a souvlaki come together. This is optional and does not have to be there.

https://gr.pinboardly.example/pin/100000000000000005/

https://gr.pinboardly.example/pin/100000000000000006/

https://gr.pinboardly.example/pin/100000000000000007/

https://gr.pinboardly.example/pin/100000000000000008/

Target Market(s)

London

Font styles to use
Serif
Sans Serif

Colors
abd037
3277b5
33a6d7

Requirements
Must have
• Build your own souvlaki section. See description for examples.

Pictures for starters and salads.

Should be elegant
Nice to have
• Incorporate our relevant meal deals on the souvlaki pita section

```html
<!DOCTYPE html>
<html lang="en">
<head>
<meta charset="utf-8">
<title>Souvliaki Bar and Grill – Menu</title>
<link href="https://fonts.googleapis.com/css2?family=Chewy&family=Varela+Round&family=Mulish:wght@300;400;600&display=swap" rel="stylesheet">
<style>
  :root {
    --backdrop: #d1dcbd;
    --board: #1d1d1d;
    --board-light: #2a2a2a;
    --green: #7fa43a;
    --green-bright: #9bc146;
    --ink: #f4f4f4;
    --muted: #bdbdbd;
    --rule: #cfcfcf;
    --display: "Chewy", "Comic Sans MS", "Chalkboard SE", cursive;
    --body: "Varela Round", "Mulish", "Trebuchet MS", sans-serif;
    --light: "Mulish", "Varela Round", sans-serif;
  }
  * { box-sizing: border-box; margin: 0; padding: 0; }
  html, body { width: 1200px; height: 1200px; overflow: hidden; }
  body {
    background: var(--backdrop);
    font-family: var(--body);
    color: var(--ink);
    position: relative;
  }
  .page {
    position: absolute; top: 247px; width: 504px; height: 712px;
    background: radial-gradient(ellipse at 40% 30%, var(--board-light), var(--board) 70%);
    overflow: hidden;
  }
  .page--wraps { left: 63px; }
  .page--grill { left: 640px; }

  /* header */
  .corner-pattern {
    position: absolute; top: 0; width: 45px; height: 88px;
    background: linear-gradient(90deg, #777 0 2px, transparent 2px 6px, var(--green) 6px 8px, transparent 8px 12px);
    opacity: .55;
  }
  .brand {
    position: absolute; left: 78px; top: 34px; width: 115px;
    font-family: var(--display); font-size: 21px; line-height: 24px;
    color: var(--ink); text-align: center; letter-spacing: 1px;
  }
  .brand-divider { position: absolute; left: 225px; top: 32px; width: 5px; height: 92px; border-left: 2px solid #ddd; border-right: 2px solid #ddd; }
  .title-souvliaki {
    position: absolute; left: 262px; top: 33px;
    font-family: var(--display); font-size: 38px; color: var(--green); line-height: 1;
  }
  .title-grill {
    position: absolute; left: 262px; top: 78px;
    font-family: var(--display); font-size: 38px; color: var(--ink); line-height: 1; letter-spacing: .5px;
  }

  /* rules */
  .rule-dotted { position: absolute; border-top: 1.5px dotted var(--rule); }
  .rule-dotted-v { position: absolute; border-left: 1.5px dotted var(--rule); }
  .rule-hatched { position: absolute; height: 5px; background: repeating-linear-gradient(115deg, #cfcfcf 0 1px, transparent 1px 3px); }

  .section-title {
    position: absolute; left: 0; width: 100%; text-align: center;
    font-family: var(--display); font-weight: 400; color: var(--green); font-size: 23px; line-height: 1;
  }
  .intro { position: absolute; left: 0; width: 100%; text-align: center; font-size: 8.5px; }
  .intro em { font-style: normal; color: var(--green-bright); }

  /* steps */
  .step-num {
    position: absolute; width: 34px; height: 34px; border-radius: 50%;
    background: var(--green); outline: 1.5px dotted #fff; outline-offset: 2px;
    font-family: var(--display); font-size: 25px; color: #fff;
    display: flex; align-items: center; justify-content: center;
  }
  .step-head { position: absolute; font-family: var(--display); color: var(--green); font-size: 14px; line-height: 15.5px; white-space: nowrap; }
  .list { position: absolute; list-style: none; font-size: 7.6px; line-height: 12.7px; white-space: nowrap; }
  .list--wrap { white-space: normal; }
  .price { color: var(--green-bright); margin-left: 4px; }
  .note { font-family: var(--light); font-weight: 300; color: var(--muted); }

  .offer-kicker { position: absolute; font-family: var(--display); color: var(--green); font-size: 13px; }
  .offer-name { position: absolute; font-family: var(--display); color: var(--ink); font-size: 14px; white-space: nowrap; }
  .offer-line { position: absolute; font-family: var(--display); color: var(--green); font-size: 13px; line-height: 16px; }
  .offer-line b { color: var(--ink); font-weight: 400; font-family: var(--body); }

  /* platters */
  .platter-title { position: absolute; font-family: var(--display); color: var(--green); font-size: 14px; text-align: center; }
  .platter-desc { position: absolute; font-size: 6.5px; line-height: 9px; text-align: center; }
  .label { color: var(--green-bright); text-transform: uppercase; }
  .photo { position: absolute; border: 1px solid #ddd; }
  .photo--fries { background: linear-gradient(135deg, #5c8fc4, #e9d9a9 45%, #b77b3c 70%, #5c8fc4); }
  .photo--gyros { background: linear-gradient(135deg, #f3f1ec, #8a5a2e 35%, #d2402f 65%, #f3f1ec); }
  .photo--sausage { background: linear-gradient(135deg, #5c8fc4, #e7c76a 40%, #a5352a 65%, #5c8fc4); }
  .photo--steak { background: linear-gradient(135deg, #d8d0d6, #5a3a2a 40%, #c84a3a 70%, #e6e6e6); }

  /* grill rows */
  .dish-title { position: absolute; left: 146px; max-width: 132px; font-family: var(--display); color: var(--green); font-size: 10.5px; line-height: 12px; white-space: nowrap; }
  .dish-desc { position: absolute; left: 146px; width: 128px; font-family: var(--light); font-size: 8.5px; line-height: 11.4px; font-weight: 300; color: var(--muted); }
</style>
</head>
<body>

<section class="page page--wraps">
  <div class="corner-pattern" role="img" aria-label="Greek key stripe ornament" style="left:30px"></div>
  <div class="corner-pattern" role="img" aria-label="Greek key stripe ornament" style="left:425px"></div>
  <div class="brand">OLIVE<br>BRANCH<br>KITCHEN</div>
  <div class="brand-divider"></div>
  <div class="title-souvliaki">Souvliaki</div>
  <div class="title-grill">Bar and Grill</div>

  <div class="rule-dotted" style="left:30px;width:444px;top:134px"></div>
  <h2 class="section-title" style="top:141px">Our Souvliaki Pita Wrap&nbsp; 5.50</h2>
  <p class="intro" style="top:166px">Get a whole meal containing protein, sauce and salad with our delicious <em>Greek Pita Wraps!</em></p>
  <div class="rule-dotted" style="left:30px;width:444px;top:181px"></div>
  <div class="rule-dotted-v" style="left:252px;top:181px;height:271px"></div>

  <div class="step-num" style="left:33px;top:195px">1</div>
  <div class="step-head" style="left:82px;top:193px">Choose a base.</div>
  <ul class="list" style="left:82px;top:213px">
    <li>Chicken<span class="price">0.50</span></li>
    <li>Pork<span class="price">0.50</span></li>
    <li>Gyros Chicken<span class="price">1.50</span></li>
    <li>Gyros Pork<span class="price">1.50</span></li>
    <li>Mixed Gyros (chicken and pork)<span class="price">2.00</span></li>
    <li>Kebab (lamb+beef)<span class="price">0.50</span></li>
    <li>Sausage<span class="price">0.50</span></li>
    <li>Haloumi (V)<span class="price">0.50</span></li>
  </ul>

  <div class="step-num" style="left:265px;top:195px">2</div>
  <div class="step-head" style="left:314px;top:193px">Add one of our delicious<br>home made sauces.</div>
  <ul class="list" style="left:314px;top:228px">
    <li>Tzatziki (V)</li><li>Tyrokafteri (V)</li><li>Burger Sauce</li>
  </ul>
  <div class="rule-dotted" style="left:263px;width:211px;top:273px"></div>

  <div class="step-num" style="left:267px;top:285px">3</div>
  <div class="step-head" style="left:314px;top:285px">Finalise it with the<br>ingredients of your choice.</div>
  <ul class="list" style="left:314px;top:321px">
    <li class="note">You can add multiple ingredients.</li>
    <li>Fries</li><li>Tomatoes</li><li>Onions</li>
  </ul>

  <div class="rule-dotted" style="left:30px;width:212px;top:321px"></div>
  <div class="step-num" style="left:34px;top:334px">4</div>
  <div class="step-head" style="left:84px;top:328px">Feeling Hungry?<br>Add extras:</div>
  <ul class="list" style="left:84px;top:367px">
    <li>Double Pita Bread<span class="price">1.00</span></li>
    <li>Add Pork Skewer<span class="price">2.50</span></li>
    <li>Add Chicken Skewer<span class="price">2.50</span></li>
    <li>Add Kebab (lamb+beef)<span class="price">2.50</span></li>
    <li>Add Sausage<span class="price">2.50</span></li>
    <li>Add Haloumi<span class="price">1.90</span></li>
  </ul>

  <div class="rule-dotted" style="left:263px;width:211px;top:374px"></div>
  <div class="offer-kicker" style="left:268px;top:379px">TRY OUR</div>
  <div class="offer-name" style="left:268px;top:394px">Double Souvlaki Pita Wrap Offer...</div>
  <div class="offer-line" style="left:268px;top:414px">Buy two wraps for <b>10.5</b><br>Takeout only!</div>

  <div class="rule-dotted" style="left:30px;width:444px;top:452px"></div>
  <h2 class="section-title" style="top:457px">Our Open Souvliaki Platters</h2>
  <div class="rule-dotted" style="left:30px;width:444px;top:485px"></div>
  <div class="rule-dotted-v" style="left:252px;top:485px;height:188px"></div>

  <div class="platter-title" style="left:30px;width:200px;top:492px">Skewers Platter&nbsp;&nbsp; 10.00</div>
  <p class="platter-desc" style="left:30px;width:210px;top:510px">Homemade souvlaki is taken from the best part of the meat to create the perfect succulent grilled experience.</p>
  <div class="photo photo--fries" role="img" aria-label="Photo of skewers with fries on a plate" style="left:32px;top:535px;width:91px;height:44px"></div>
  <ul class="list" style="left:160px;top:534px">
    <li class="label">Sides</li><li>Fries</li><li>Side Salad<span class="price">2.50</span></li>
  </ul>
  <ul class="list" style="left:31px;top:582px">
    <li class="label">Meat Options</li>
    <li>2 x Chicken Skewers</li>
    <li>3 x Chicken Skewers<span class="price">3.00</span></li>
    <li>2 x Pork Skewers</li>
    <li>3 x Pork Skewers<span class="price">3.00</span></li>
    <li>2 x Kebab (lamb+beef)</li>
    <li>3 x Kebab (lamb+beef)<span class="price">3.00</span></li>
  </ul>
  <ul class="list" style="left:160px;top:583px">
    <li class="label">Extras</li>
    <li>Extra Haloumi<span class="price">3.50</span></li>
    <li>Extra Tzatziki<span class="price">3.00</span></li>
  </ul>
  <ul class="list" style="left:160px;top:631px">
    <li class="label">Pita Bread</li><li>1 x Pita</li><li>2 x Pita<span class="price">1.00</span></li>
  </ul>

  <div class="platter-title" style="left:274px;width:200px;top:492px">Gyros Platter&nbsp;&nbsp; 13.00</div>
  <p class="platter-desc" style="left:264px;width:212px;top:510px">Generous portion served with refreshing tzatziki sauce, pita bread, fries, onion, tomatoes and lettuce.</p>
  <div class="rule-dotted-v" style="left:368px;top:535px;height:135px"></div>
  <ul class="list list--wrap" style="left:262px;top:532px;width:100px;line-height:10.4px">
    <li class="label" style="margin-bottom:3px">Meat Options</li>
    <li>Meat Options</li>
    <li>Chicken Gyros 200gr</li>
    <li>Pork Gyros 200gr</li>
    <li>Mixed Gyros (chicken and pork) 200gr<span class="price">1.00</span></li>
    <li>Chicken Gyros 300gr<span class="price">3.50</span></li>
    <li>Pork Gyros 300gr<span class="price">3.50</span></li>
    <li>Mixed Gyros (chicken and pork) 300gr<span class="price">4.50</span></li>
  </ul>
  <div class="photo photo--gyros" role="img" aria-label="Photo of gyros platter with fries and tomatoes" style="left:384px;top:535px;width:91px;height:44px"></div>
  <ul class="list" style="left:384px;top:586px">
    <li class="label">Extras</li>
    <li>Extra Haloumi<span class="price">3.50</span></li>
    <li>Extra Tzatziki<span class="price">3.00</span></li>
  </ul>
  <ul class="list" style="left:384px;top:633px">
    <li class="label">Pita Bread</li><li>1 x Pita</li><li>2 x Pita<span class="price">1.00</span></li>
  </ul>
  <div class="rule-hatched" style="left:33px;width:440px;top:675px"></div>
</section>

<section class="page page--grill">
  <div class="corner-pattern" role="img" aria-label="Greek key stripe ornament" style="left:30px"></div>
  <div class="corner-pattern" role="img" aria-label="Greek key stripe ornament" style="left:425px"></div>
  <div class="brand">OLIVE<br>BRANCH<br>KITCHEN</div>
  <div class="brand-divider"></div>
  <div class="title-souvliaki">Souvliaki</div>
  <div class="title-grill">Bar and Grill</div>

  <div class="rule-dotted" style="left:30px;width:444px;top:138px"></div>
  <div class="rule-hatched" style="left:32px;width:138px;top:151px"></div>
  <h2 class="section-title" style="top:142px">From Our Grill</h2>
  <div class="rule-hatched" style="left:335px;width:137px;top:151px"></div>
  <div class="rule-dotted" style="left:30px;width:444px;top:174px"></div>

  <div class="photo photo--fries" role="img" aria-label="Photo of grilled fillets with fries" style="left:39px;top:188px;width:97px;height:78px"></div>
  <div class="dish-title" style="top:198px">FILLETS&nbsp; 13.00</div>
  <p class="dish-desc" style="top:211px">Grilled tender pork or chicken fillets topped with an oregano and lemon sauce. Served with fries.</p>
  <ul class="list" style="left:282px;top:193px">
    <li class="label">Meat Options</li><li>Chicken (Halal) Fillet</li><li>Pork Fillet</li>
    <li class="label">Sides</li><li>Fries</li><li>Side Salad<span class="price">2.50</span></li>
  </ul>
  <ul class="list" style="left:386px;top:193px">
    <li class="label">Extras</li><li>Extra Haloumi<span class="price">3.50</span></li><li>Extra Tzatziki<span class="price">3.00</span></li>
    <li class="label">Pita Bread</li><li>1 x Pita</li><li>2 x Pita<span class="price">1.00</span></li>
  </ul>
  <div class="rule-dotted" style="left:30px;width:444px;top:281px"></div>

  <div class="photo photo--sausage" role="img" aria-label="Photo of grilled village sausages with fries" style="left:39px;top:295px;width:97px;height:78px"></div>
  <div class="dish-title" style="top:305px">VILLAGE SAUSAGES&nbsp; 9.50</div>
  <p class="dish-desc" style="top:318px">Two large grilled sausages from Thrace served with mustard or lemon dressing. Served with fries.</p>
  <ul class="list" style="left:282px;top:300px">
    <li class="label">Dressing</li><li>Mustard</li><li>Lemon</li>
    <li class="label">Sides</li><li>Fries</li><li>Side Salad<span class="price">2.50</span></li>
  </ul>
  <ul class="list" style="left:386px;top:300px">
    <li class="label">Extras</li><li>Extra Haloumi<span class="price">3.50</span></li><li>Extra Tzatziki<span class="price">3.00</span></li>
    <li class="label">Pita Bread</li><li>1 x Pita</li><li>2 x Pita<span class="price">1.00</span></li>
  </ul>
  <div class="rule-dotted" style="left:30px;width:444px;top:385px"></div>

  <div class="photo photo--steak" role="img" aria-label="Photo of ribeye steak with Greek salad" style="left:39px;top:398px;width:97px;height:78px"></div>
  <div class="dish-title" style="top:408px">RIBEYE STEAK&nbsp; 24.50</div>
  <p class="dish-desc" style="top:421px">Highly desired cut of meat has full flavour, soft and rich texture and juicy finish.</p>
  <ul class="list" style="left:282px;top:403px">
    <li class="label" style="text-transform:none">Preferred Cooking</li><li>Rare/ Medium Rare</li>
    <li style="line-height:10px;padding:1px 0 2px">Medium/ Medium Well/<br>Well done</li>
    <li class="label">Sides</li><li>Fries</li><li>Side Salad<span class="price">2.50</span></li>
  </ul>
  <ul class="list" style="left:386px;top:403px">
    <li class="label">Extras</li><li>Extra Haloumi<span class="price">3.50</span></li><li>Extra Tzatziki<span class="price">3.00</span></li>
    <li class="label">Pita Bread</li><li>1 x Pita</li><li>2 x Pita<span class="price">1.00</span></li>
  </ul>
  <div class="rule-dotted" style="left:30px;width:444px;top:496px"></div>

  <div class="photo photo--fries" role="img" aria-label="Photo of lamb cutlets with fries" style="left:39px;top:505px;width:97px;height:78px"></div>
  <div class="dish-title" style="top:516px">LAMB CUTLETS&nbsp; 16.00</div>
  <p class="dish-desc" style="top:529px">Tender lamb cutlets grilled to perfection and served with fries.</p>
  <ul class="list" style="left:282px;top:511px">
    <li class="label">Sides</li><li>Fries</li><li>Side Salad<span class="price">2.50</span></li>
    <li class="label">Extras</li><li>Extra Haloumi<span class="price">3.50</span></li><li>Extra Tzatziki<span class="price">3.00</span></li>
  </ul>
  <ul class="list" style="left:386px;top:511px">
    <li class="label">Pita Bread</li><li>1 x Pita</li><li>2 x Pita<span class="price">1.00</span></li>
  </ul>
  <div class="rule-dotted" style="left:30px;width:444px;top:592px"></div>

  <div class="photo photo--steak" role="img" aria-label="Photo of sirloin steak with Greek salad" style="left:39px;top:602px;width:97px;height:78px"></div>
  <div class="dish-title" style="top:601px">SIRLOIN STEAK&nbsp; 24.50</div>
  <p class="dish-desc" style="top:614px">Highly desired cut of meat has a beefier flavour, less fat and medium tender, as it comes from an area where muscles get more exercise</p>
  <ul class="list" style="left:282px;top:601px">
    <li class="label" style="text-transform:none">Preferred Cooking</li><li>Rare/ Medium Rare</li>
    <li style="line-height:10px;padding:1px 0 2px">Medium/ Medium Well/<br>Well done</li>
    <li class="label">Sides</li><li>Fries</li><li>Side Salad<span class="price">2.50</span></li>
  </ul>
  <ul class="list" style="left:386px;top:601px">
    <li class="label">Pita Bread</li><li>1 x Pita</li><li>2 x Pita<span class="price">1.00</span></li>
  </ul>
  <div class="rule-hatched" style="left:33px;width:440px;top:691px"></div>
</section>

</body>
</html>
```